Marketing Skill "Workouts"; Design for an e-mail attachment highlighting Marketing training subjects

I am a freelance marketing trainer based in Singapore and need to e-mail out an attachment (probably saved as a PDF) to potential clients showing the training services I offer. These clients are all large blue-chip multinational companies so the attachment needs to look professional/high quality when opened on a computer.

My Company is called "Clearpath Marketing" (logo attached)

I am assuming the size should be A4 one sided colour.

I have attached some files that show best-attempts so far. These contain the key information, but the layouts all still look rather pedestrian. I am looking for something that looks a bit more dynamic but remains clear/easy to read.

Target Market(s)

HR/Marketing managers in multinational firms, mainly consumer goods

Industry/Entity Type

Marketing

Font styles to use
Sans Serif

Colors

Designer to choose colors to be used in the design.

Requirements
Must have
• Must look modern, up-to-date, professional.
Should not have
• Not gimmicky, like a cheap deal

```html
<!DOCTYPE html>
<html lang="en">
<head>
<meta charset="utf-8">
<title>Marketing Skill Workouts – Clearpath Marketing</title>
<link rel="stylesheet" href="https://fonts.googleapis.com/css2?family=Oswald:wght@500&family=Open+Sans:ital,wght@0,700;1,700&display=swap">
<style>
  :root {
    --cyan: #2ad6dc;
    --white: #ffffff;
    --maroon: #8a1c1e;
    --maroon-deep: #6e1214;
    --teal-dark: #0a3134;
    --teal-mid: #124a4d;
    --ink: #1d1d1d;
    --wall-light: #8a8a8a;
    --wall-dark: #2b2b2b;
  }
  * { box-sizing: border-box; margin: 0; padding: 0; }
  html, body { width: 848px; height: 1200px; overflow: hidden; background: var(--white); }
  body { font-family: "Open Sans", Arial, sans-serif; color: var(--white); }

  .sheet { position: relative; width: 848px; height: 1200px; overflow: hidden; }

  .backdrop {
    position: absolute; inset: 0 0 214px 0;
    background:
      radial-gradient(ellipse 70% 45% at 60% 10%, #a9a9a9 0%, transparent 70%),
      linear-gradient(180deg, var(--wall-light) 0%, #5a5a5a 35%, var(--wall-dark) 75%, #1e1e1e 100%);
  }
  .figure-area {
    position: absolute; left: 520px; top: 140px; width: 328px; height: 846px;
    background: linear-gradient(180deg, rgba(120,120,120,0.35) 0%, rgba(90,90,90,0.55) 50%, rgba(60,60,60,0.4) 100%);
  }
  .bar-area {
    position: absolute; left: 90px; top: 20px; width: 640px; height: 160px;
    background: linear-gradient(90deg, rgba(230,230,230,0.2), rgba(255,255,255,0.35) 60%, rgba(230,230,230,0.15));
    border-radius: 4px;
  }

  .brand-name {
    position: absolute; right: 154px; top: 64px;
    font-size: 31px; font-weight: 700; color: var(--ink); line-height: 1;
  }

  .headline {
    position: absolute; left: 60px; top: 186px;
    font-family: "Oswald", "Arial Narrow", sans-serif; font-weight: 500;
    font-size: 90px; line-height: 96px; color: var(--cyan); letter-spacing: 0.5px;
  }
  .question { position: absolute; left: 62px; top: 406px; font-size: 33px; font-weight: 700; letter-spacing: 0.8px; }
  .lede { position: absolute; left: 62px; top: 462px; width: 510px; font-size: 23.5px; font-weight: 700; line-height: 32px; }

  .section-tab {
    position: absolute; top: 595px; height: 54px;
    background: linear-gradient(180deg, var(--maroon), var(--maroon-deep));
    font-size: 28px; font-weight: 700; padding-left: 24px; line-height: 54px; letter-spacing: 0.5px;
  }
  .tab-topics { left: 62px; width: 328px; }
  .tab-benefits { left: 402px; width: 326px; }

  .topics { position: absolute; left: 70px; top: 678px; width: 290px; list-style: none; }
  .topics li { position: relative; padding-left: 16px; font-size: 15.5px; font-weight: 700; line-height: 18px; margin-bottom: 8px; }
  .topics li::before { content: "•"; position: absolute; left: 0; }

  .benefits { position: absolute; left: 410px; top: 672px; width: 272px; list-style: none; }
  .benefits li { position: relative; padding-left: 20px; font-size: 18px; font-weight: 700; line-height: 23px; margin-bottom: 18px; }
  .benefits li::before { content: "»"; position: absolute; left: 0; color: var(--white); }

  .why-band {
    position: absolute; left: 0; top: 986px; width: 848px; height: 166px;
    background: linear-gradient(90deg, var(--teal-dark) 0%, var(--teal-mid) 55%, var(--teal-dark) 100%);
  }
  .why-title {
    position: absolute; left: 68px; top: -4px;
    font-family: "Oswald", "Arial Narrow", sans-serif; font-weight: 500; font-size: 56px; color: var(--cyan);
  }
  .why-claim { position: absolute; left: 326px; top: 20px; font-size: 25.5px; font-weight: 700; font-style: italic; }
  .why-point { position: absolute; top: 86px; padding-left: 22px; font-size: 16px; font-weight: 700; line-height: 20px; }
  .why-point::before { content: "»"; position: absolute; left: 0; color: var(--cyan); }
  .why-point-a { left: 64px; width: 250px; }
  .why-point-b { left: 312px; width: 494px; }

  .contact-bar {
    position: absolute; left: 0; top: 1152px; width: 848px; height: 48px;
    background: var(--white); color: var(--ink);
    display: flex; justify-content: space-between; align-items: center; padding: 0 64px 0 50px;
  }
  .contact { display: flex; align-items: center; gap: 10px; font-size: 21px; font-weight: 700; }
  .contact-icon { width: 30px; height: 30px; border-radius: 50%; background: var(--maroon); display: flex; align-items: center; justify-content: center; }
</style>
</head>
<body>
<main class="sheet">
  <div class="backdrop" role="img" aria-label="Textured grey wall background"></div>
  <div class="bar-area" role="img" aria-label="White graph-style bar chart and horizontal bar being gripped"></div>
  <div class="figure-area" role="img" aria-label="Photo of a young businessman in a grey suit and teal shirt hanging from a bar with one hand"></div>

  <header class="brand-name">Clearpath Marketing</header>

  <h1 class="headline">Marketing Skill<br>'Workouts'</h1>
  <p class="question">NO TIME TO LEARN?</p>
  <p class="lede">- Problem solved with 1 day intensive workshops that will drive business growth and motivate your team.</p>

  <div class="section-tab tab-topics">KEY TOPICS</div>
  <div class="section-tab tab-benefits">KEY BENEFITS</div>

  <ul class="topics">
    <li>Developing strong brand plans</li>
    <li>Writing inspiring briefs/creative evaluation</li>
    <li>Shopper marketing/developing retail promotions</li>
    <li>Brilliant launch management</li>
    <li>Improving marketing R.O.I.</li>
    <li>Driving brand growth without product innovation</li>
    <li>Insight/concept development</li>
    <li>Integrating digital channels</li>
    <li>Creatvitiy and idea generation</li>
  </ul>

  <ul class="benefits">
    <li>Latest in world-class thinking/tools/case studies</li>
    <li>Ability to 'customise' to address your specific business issue</li>
    <li>Take-away 'checklists' to embed behaviours and skills</li>
    <li>Asian context/relevance</li>
    <li>Proven quality</li>
  </ul>

  <section class="why-band">
    <h2 class="why-title">Why Me?</h2>
    <p class="why-claim">World Class Quality without the costs</p>
    <p class="why-point why-point-a">The latest thinking, made practical and actionable.</p>
    <p class="why-point why-point-b">20 years of business experience combined with 10 years of proven training/ facilitation for major blue-chip" clients, regularly acoring 90%+ satisfaction.</p>
  </section>

  <footer class="contact-bar">
    <div class="contact">
      <span class="contact-icon">
        <svg width="18" height="18" viewBox="0 0 24 24" fill="none" stroke="#fff" stroke-width="2.6"><circle cx="12" cy="12" r="4"/><path d="M16 8v5a3 3 0 0 0 6 0v-1a10 10 0 1 0-4 8"/></svg>
      </span>
      hello@clearpath-marketing.com
    </div>
    <div class="contact">
      <span class="contact-icon">
        <svg width="16" height="18" viewBox="0 0 16 22"><rect x="2" y="1" width="12" height="20" rx="2" fill="none" stroke="#fff" stroke-width="2"/><circle cx="8" cy="17" r="1.3" fill="#fff"/></svg>
      </span>
      +65 9000 4417
    </div>
  </footer>
</main>
</body>
</html>
```